Quorvex - Automated robotic Inspection with AI need new business cards

We need a new design of our business cards. The company is focused on automated quality control at high speed with unmatched results. We have a logo but need a more forward leaning business card that shows that we are delivering cutting edge technology.

Contact Information for Business Card

Name
Position
Adress
Phone
Email
e.g.
Lena Holmqvist
Chief Financial Officer (CFO)

Quorvex Sweden AB
Bruksvägen 14, SE-175 43 JÄRFÄLLA, Sweden
Mobile: +46735 21 47 83 | Office: +46 8 61 94 27
www.quorvex-example.com

Font styles to use
Sans Serif

```html
<!DOCTYPE html>
<html lang="en">
<head>
<meta charset="utf-8">
<title>Quorvex Business Card</title>
<link href="https://fonts.googleapis.com/css2?family=Roboto:wght@400;500;700&display=swap" rel="stylesheet">
<style>
  :root {
    --page-bg: #e6e6e6;
    --card-dark: #161616;
    --brand-blue: #1f5a88;
    --name-blue: #1e5d92;
    --text-grey: #a3a3a3;
    --rule-grey: #6a6a6a;
    --ink-dark: #1c1c1c;
  }
  * { margin: 0; padding: 0; box-sizing: border-box; }
  html, body {
    width: 1125px; height: 1200px; overflow: hidden;
    background: var(--page-bg);
    font-family: "Roboto", Arial, sans-serif;
  }
  .card {
    position: absolute; left: 150px; width: 826px; height: 472px;
    box-shadow: 0 2px 4px rgba(0,0,0,0.35);
  }
  .card--front { top: 98px; background: var(--card-dark); border-bottom: 11px solid var(--brand-blue); }
  .card--back { top: 631px; background: var(--brand-blue); }

  .brand-name {
    position: absolute; font-weight: 500; letter-spacing: 1px;
    display: flex; align-items: center; gap: 14px;
  }
  .brand-mark { border-radius: 50%; display: block; }
  .card--front .brand-name { left: 56px; top: 72px; font-size: 52px; color: var(--brand-blue); }
  .card--front .brand-mark { width: 34px; height: 34px; background: var(--brand-blue); }
  .card--back .brand-name {
    left: 0; right: 0; top: 178px; justify-content: center;
    font-size: 72px; color: var(--ink-dark);
  }
  .card--back .brand-mark { width: 46px; height: 46px; background: var(--ink-dark); }

  .person { position: absolute; left: 56px; top: 250px; }
  .person__name { font-size: 26px; font-weight: 700; color: var(--name-blue); line-height: 1.2; }
  .person__role { font-size: 18px; font-weight: 500; color: var(--text-grey); margin-top: 2px; }

  .divider { position: absolute; left: 56px; right: 68px; top: 324px; height: 1px; background: var(--rule-grey); }

  .contact-list { position: absolute; left: 58px; top: 343px; list-style: none; }
  .contact-list li {
    display: flex; align-items: center; gap: 12px;
    font-size: 18px; color: var(--text-grey); height: 23.5px;
  }
  .contact-list svg { width: 15px; height: 15px; fill: var(--brand-blue); flex: none; }

  .address {
    position: absolute; right: 63px; top: 343px; text-align: right;
    font-size: 18px; color: var(--text-grey); line-height: 23.5px; font-style: normal;
  }
  .address .accent { color: var(--brand-blue); }

  .back-web {
    position: absolute; left: 0; right: 0; top: 405px; text-align: center;
    font-size: 17px; letter-spacing: 3px; color: var(--ink-dark);
  }
</style>
</head>
<body>
  <section class="card card--front">
    <div class="brand-name"><span class="brand-mark"></span>Quorvex</div>

    <div class="person">
      <div class="person__name">Lena Holmqvist</div>
      <div class="person__role">Chief Financial Officer (CFO)</div>
    </div>

    <div class="divider"></div>

    <ul class="contact-list">
      <li>
        <svg viewBox="0 0 24 24" aria-hidden="true"><path d="M6.6 10.8a15.1 15.1 0 0 0 6.6 6.6l2.2-2.2c.3-.3.7-.4 1-.2 1.1.4 2.3.6 3.6.6.6 0 1 .4 1 1V20c0 .6-.4 1-1 1A17 17 0 0 1 3 4c0-.6.4-1 1-1h3.5c.6 0 1 .4 1 1 0 1.3.2 2.5.6 3.6.1.3 0 .7-.2 1z"/></svg>
        +46 8 61 94 27
      </li>
      <li>
        <svg viewBox="0 0 24 24" aria-hidden="true"><path d="M7 1h10a2 2 0 0 1 2 2v18a2 2 0 0 1-2 2H7a2 2 0 0 1-2-2V3a2 2 0 0 1 2-2zm0 3v14h10V4zm5 15.5a1 1 0 1 0 0 2 1 1 0 0 0 0-2z"/></svg>
        +46735 21 47 83
      </li>
      <li>
        <svg viewBox="0 0 24 24" aria-hidden="true"><path d="M3 6h18v12H3zm1.5 1.5v.4L12 13l7.5-5.1v-.4z"/></svg>
        info@quorvex-example.com
      </li>
    </ul>

    <address class="address">
      Quorvex Sweden AB, Bruksvägen 14<br>
      SE-175 43 JÄRFÄLLA, Sweden<br>
      www.<span class="accent">quorvex-example</span>.com
    </address>
  </section>

  <section class="card card--back">
    <div class="brand-name"><span class="brand-mark"></span>Quorvex</div>
    <div class="back-web">www.quorvex-example.com</div>
  </section>
</body>
</html>
```